beyond the logo to paper
introduce logo to paper
Project: beyond the logo to paper
beyond the logo to paper -
Creative Brief
Use same font as used in my logo
Gordon T. Pellwick
Operations
P.O. Box 518 Fernwold, MD 21694
glowpath2day@vexmail.example
TRQB 42615
looking to use kraft style paper; or atleast 100% re-cycled with no gloss; need to show resourcefulness when in hand; like various shapes; want the card to be a sales employee for the business
if the front contains the contact information then the back will either have a brief testimony about who we are, or offer various tips when hiring a contractor.

```html
<!DOCTYPE html>
<html lang="en">
<head>
<meta charset="utf-8">
<title>Crestvale Stationery Set</title>
<link href="https://fonts.googleapis.com/css2?family=Roboto:wght@400;700;900&display=swap" rel="stylesheet">
<style>
:root{
  --bg:#000;
  --navy:#0d2a7a;
  --blue:#1848c8;
  --sky:#3aa0e2;
  --green:#7ac142;
  --paper:#fff;
  --ink:#333;
  --muted:#8a8a8a;
}
*{margin:0;padding:0;box-sizing:border-box}
html,body{width:1200px;height:874px;overflow:hidden;background:var(--bg)}
body{position:relative;font-family:"Roboto",Arial,sans-serif;color:var(--ink)}
.piece{position:absolute;overflow:hidden}
.band{position:absolute;left:0;right:0;background:linear-gradient(90deg,var(--navy),var(--blue) 45%,var(--sky))}
.brand{display:flex;align-items:center;gap:6px;font-weight:900;color:var(--navy);letter-spacing:.5px;white-space:nowrap}
.brand .mark{display:inline-block;background:var(--green)}
.contact{font-size:8px;line-height:10px;color:var(--navy);font-weight:700;white-space:nowrap}
.contact-grid{display:flex;gap:16px}

/* envelope */
.envelope{left:43px;top:19px;width:586px;height:243px;background:var(--paper)}
.envelope .top{top:0;height:34px}
.envelope .flap{position:absolute;left:0;top:0;width:586px;height:243px}
.envelope .bottom{bottom:0;height:30px}
.envelope .brand{position:absolute;left:30px;top:120px;font-size:24px}
.envelope .brand .mark{width:20px;height:20px}
.envelope .contact-grid{position:absolute;left:210px;top:124px}
.envelope .license{position:absolute;left:30px;bottom:9px;font-size:7px;color:#fff;font-weight:700}

/* folder */
.folder{left:43px;top:307px;width:586px;height:545px;background:var(--paper)}
.folder svg{position:absolute;left:0;top:0}
.folder .ghost{position:absolute;left:40px;top:150px;font-size:44px;opacity:.13}
.folder .ghost .mark{width:34px;height:34px}
.folder .license{position:absolute;left:20px;bottom:20px;font-size:7px;color:#fff;font-weight:700}
.folder .pocket-brand{position:absolute;left:392px;top:338px;font-size:16px;color:var(--navy)}
.folder .pocket-brand .mark{width:14px;height:14px}
.folder .pocket-contact{position:absolute;left:330px;top:378px;color:#fff}

/* letterhead */
.letterhead{left:643px;top:19px;width:533px;height:610px;background:var(--paper)}
.letterhead .top{top:0;height:8px}
.letterhead .body{position:absolute;left:34px;top:34px;right:34px;font-size:8px;line-height:11.5px;color:var(--muted);text-align:justify}
.letterhead .body p{margin-bottom:12px}
.letterhead .brand{position:absolute;left:34px;top:520px;font-size:26px}
.letterhead .brand .mark{width:22px;height:22px}
.letterhead .contact-grid{position:absolute;left:250px;top:522px}
.letterhead .bottom{bottom:0;height:36px}
.letterhead .license{position:absolute;left:34px;bottom:14px;font-size:7px;color:#fff;font-weight:700}

/* business cards */
.card-front{left:677px;top:643px;width:222px;height:122px;background:var(--paper)}
.card-front .brand{position:absolute;left:10px;top:18px;font-size:13px}
.card-front .brand .mark{width:10px;height:10px}
.card-front .person{position:absolute;right:10px;top:16px;text-align:right}
.card-front .name{font-size:9px;font-weight:700;color:var(--navy)}
.card-front .role{font-size:7px;color:var(--muted)}
.card-front .contact{position:absolute;left:10px;top:56px;font-size:6.5px;line-height:8.5px}
.card-front .bottom{bottom:0;height:16px}
.card-back{left:912px;top:643px;width:264px;height:122px;background:linear-gradient(135deg,var(--navy),var(--blue) 55%,var(--sky))}
.card-back .email{position:absolute;left:14px;bottom:10px;font-size:7px;color:#fff}
.card-back .stripe{position:absolute;left:0;right:0;top:0;height:6px;background:var(--green)}
</style>
</head>
<body>

<section class="piece envelope">
  <div class="band top"></div>
  <svg class="flap" viewBox="0 0 586 243" aria-hidden="true">
    <path d="M0 34 L240 100 L586 34" fill="none" stroke="#d9e4f5" stroke-width="2"/>
  </svg>
  <div class="brand"><span class="mark"></span>CRESTVALE</div>
  <div class="contact-grid">
    <div class="contact">P.O. Box 518<br>Fernwold, MD 21694</div>
    <div class="contact">Toll Free: (800) 555-0148<br>Phone: (301) 555-0172<br>Cell: (301) 555-0139<br>Fax: (301) 555-0186</div>
  </div>
  <div class="band bottom"></div>
  <div class="license">License No.: TRQB 42615</div>
</section>

<section class="piece folder">
  <svg width="586" height="545" viewBox="0 0 586 545" aria-hidden="true">
    <defs>
      <linearGradient id="folderBlue" x1="0" x2="1">
        <stop offset="0" stop-color="#0d2a7a"/><stop offset=".5" stop-color="#1848c8"/><stop offset="1" stop-color="#3aa0e2"/>
      </linearGradient>
    </defs>
    <rect x="0" y="480" width="293" height="65" fill="url(#folderBlue)"/>
    <line x1="293" y1="0" x2="293" y2="545" stroke="#ccc" stroke-width="1"/>
    <path d="M293 270 Q440 240 586 270 L586 545 L293 545 Z" fill="url(#folderBlue)"/>
    <path d="M300 270 Q440 245 580 270" fill="none" stroke="#7ac142" stroke-width="4"/>
    <rect x="372" y="315" width="150" height="58" fill="#fff"/>
    <path d="M372 315 L386 304 M522 315 L508 304" stroke="#fff" stroke-width="3"/>
  </svg>
  <div class="brand ghost"><span class="mark"></span>CRESTVALE</div>
  <div class="license">License No.: TRQB 42615</div>
  <div class="brand pocket-brand"><span class="mark"></span>CRESTVALE</div>
  <div class="contact-grid pocket-contact">
    <div class="contact" style="color:#fff">P.O. Box 518<br>Fernwold, MD 21694</div>
    <div class="contact" style="color:#fff">Toll Free: (800) 555-0148<br>Phone: (301) 555-0172<br>Fax: (301) 555-0186</div>
  </div>
</section>

<section class="piece letterhead">
  <div class="band top"></div>
  <div class="body">
    <p>Thank you for choosing our team for your next home project. We build with care, use recycled materials where we can, and treat every house as if it were our own. Our crews arrive on time, keep the site clean, and explain each step before work begins.</p>
    <p>Thank you for choosing our team for your next home project. We build with care, use recycled materials where we can, and treat every house as if it were our own. Our crews arrive on time, keep the site clean, and explain each step before work begins.</p>
    <p>Thank you for choosing our team for your next home project. We build with care, use recycled materials where we can, and treat every house as if it were our own. Our crews arrive on time, keep the site clean, and explain each step before work begins.</p>
    <p>Thank you for choosing our team for your next home project. We build with care, use recycled materials where we can, and treat every house as if it were our own. Our crews arrive on time, keep the site clean, and explain each step before work begins.</p>
  </div>
  <div class="brand"><span class="mark"></span>CRESTVALE</div>
  <div class="contact-grid">
    <div class="contact">P.O. Box 518<br>Fernwold, MD 21694</div>
    <div class="contact">Toll Free: (800) 555-0148<br>Phone: (301) 555-0172<br>Cell: (301) 555-0139<br>Fax: (301) 555-0186</div>
  </div>
  <div class="band bottom"></div>
  <div class="license">License No.: TRQB 42615</div>
</section>

<section class="piece card-front">
  <div class="brand"><span class="mark"></span>CRESTVALE</div>
  <div class="person">
    <div class="name">Gordon T. Pellwick</div>
    <div class="role">Operations</div>
  </div>
  <div class="contact">Toll Free: (800) 555-0148<br>Phone: (301) 555-0172<br>Cell: (301) 555-0139<br>Fax: (301) 555-0186<br>P.O. Box 518 Fernwold, MD 21694</div>
  <div class="band bottom"></div>
</section>

<section class="piece card-back">
  <div class="stripe"></div>
  <div class="email">glowpath2day@vexmail.example</div>
</section>

</body>
</html>
```